An Agro-Processor Needs a Packaging Design

We need packaging designs for a range of dried fruits and jams with a family look. The line-up has five variants of dried fruits and five variants of jams (the designs to include front and back of the packaging). The entire range will be marketed under the 'Verdyx' brand name - please find the logo attached (the logo has a lock-up with the tagline). The packaging format for the dried fruits are resealable stand-up pouches and the jams are glass bottles - please find attached pictures of the packaging formats for reference.

Please find inspiration boards for the packaging design. Also find attached inspiration board for the design style required for the back of the dried fruit packaging.

For the dried fruit packaging, we need to develop a seal that conveys organic and sugar-free claims (please find attached example of a seal)

Target Market(s)

Organic and natural living enthusiasts who would pay a premium to get the best for them and their families

Industry/Entity Type

Food Production

Font styles to use
Sans Serif
Script

Colors

Designer to choose colors to be used in the design.

Requirements
Must have
• - The brand name 'verdyx' is inspired by the abundance of nature in Africa, it also connotes organic, natural, freshness, delicateness, airiness, sophistication and premium and therefore the design should project these values
• - The design styling to be fun, modern and 'simplistic'
• - Please find below the packaging copy for both dried fruits and jams
• DRIED FRUIT FRONT PACKAGING:
• LOGO: Verdyx - Sunshine in Every Bite
• FIVE VARIANT NAMES: Jolly Pineapple | Dreamy Mango | Breezy Banana | Cheeky Papaya | Dapper Jackfruit
• Dried
• DEVELOP A SEAL: 100% Organic | No Added Sugar (please see example attached)
• Ugandan Origin
• Net Weight: 100g
• DRIED FRUIT BACK COPY:
• Nature's best tasting fruits are also the healthiest which is why we have made it our mission to spread nature's love! Nourished by the tropical rains on the sun-drenched soils of Africa and cultivated by the caring hands of the local farmers, our organic range of dried fruits are nutrient-dense, high in fiber and rich in minerals. Enjoy them in your salads and cereals or simply relish them as a snack! They are diet-friendly if eaten in moderation and are a natural source of energy.
• VISUAL: Stack of Fruit Visual with arrows, each with the following claims (see examples attached in the inspiration boards):
• - 100% Organic
• - No Added Sugar
• - Nutrient-Dense
• - High in Fiber
• - Rich in Minerals
• INCLUDE: Nutritional Facts Table
• Ingredients: Mango - contains 100% fruit with no added sugars, preservatives, additives, colorings or flavorings.
• Reseal the pack to maintain freshness. Store in a cool and dry place.
• INCLUDE SPACE FOR: Batch Code / Expiry Date
• Barcode
• Produced by: Kelvane Food Industries, P. O. Box XXXXX, Kampala - Uganda.
• Find out more about us:
• Telephone: +XXX-XXX-XXXXXX
• Email: Info@KelvaneFoodIndustries.example
• www.Sociapage.example/Verdyx
• JAM FRONT COPY:
• FIVE VARIANT NAMES: Jolly Pineapple with a Hint of Ginger | Dreamy Mango with a Kiss of Vanilla | Breezy Banana with a Twist of Chocolate | Cheeky Papaya with a Pinch of Cardamon | Dapper Jackfruit with a Touch of Cinnamon
• Jam
• Ugandan Origin
• Net Weight: 400g
• JAM BACK COPY:
• Nature's best tasting fruits are also the healthiest which is why we have made it our mission to spread nature's love! Our range of jams come from fruits that have been nourished by the tropical rains on the sun-drenched soils of Africa and have been cultivated by the caring hands of the local farmers. We pride ourselves on making sure that the jams taste as delicious and look as natural as the perfectly ripened fruit! We then make it even better by pairing it with a hint of spice! Enjoy them in your breakfast or use them as a filling in baking.
• Ingredients: Mango, citric acid, sugar, pectin, vanilla
• Barcode
• Find out more about us:

```html
<!DOCTYPE html>
<html lang="en">
<head>
<meta charset="utf-8">
<title>Verdyx Jolly Pineapple – Dried Fruit Pouch Front</title>
<link href="https://fonts.googleapis.com/css2?family=Philosopher:wght@700&family=Kalam:wght@400&family=Bungee&family=Oswald:wght@500;700&display=swap" rel="stylesheet">
<style>
  :root {
    --canvas: #ffffff;
    --foil-light: #f4f4f5;
    --foil-mid: #dcdcdf;
    --band-yellow: #f3b622;
    --brand-brown: #7b5d4f;
    --tagline-pink: #e8707e;
    --orange: #ef8a2b;
    --orange-soft: #f5a93a;
    --maroon: #8e1f3f;
    --plum: #4a2a3d;
    --pattern-dark: #3b2131;
    --rule-blue: #a9c0e6;
    --ink: #111111;
    --flag-black: #1a1a1a;
    --flag-yellow: #f7d117;
    --flag-red: #d0202a;
  }
  * { margin: 0; padding: 0; box-sizing: border-box; }
  html, body { width: 974px; height: 1200px; overflow: hidden; background: var(--canvas); }
  .pouch-front { position: relative; width: 974px; height: 1200px; overflow: hidden; background: var(--canvas); }

  .border-band { position: absolute; left: 0; width: 100%; background: var(--band-yellow); }
  .border-band--top { top: 0; height: 44px; }
  .border-band--bottom { top: 1139px; height: 61px; }

  .zip-area {
    position: absolute; top: 44px; left: 0; width: 100%; height: 230px;
    background: linear-gradient(180deg, var(--foil-mid) 0%, var(--foil-light) 55%, var(--canvas) 100%);
  }

  .stripe-art { position: absolute; left: 0; top: 0; width: 974px; height: 1200px; }

  .brand-name {
    position: absolute; left: 89px; top: 290px;
    font-family: "Philosopher", sans-serif; font-weight: 700;
    font-size: 112px; line-height: 1; color: var(--brand-brown); letter-spacing: 2px;
  }
  .brand-tagline {
    position: absolute; left: 92px; top: 398px;
    font-family: "Kalam", cursive; font-size: 32px; line-height: 1.2; color: var(--tagline-pink); letter-spacing: 1px;
  }
  .variant-name {
    position: absolute; left: 92px; top: 462px;
    font-family: "Bungee", sans-serif; font-size: 42px; line-height: 1.1; color: var(--orange); letter-spacing: 2px;
  }
  .variant-rule {
    position: absolute; left: 94px; top: 514px; width: 580px;
    border-top: 4px dotted var(--orange);
  }

  .process-label {
    position: absolute; left: 553px; top: 765px;
    transform: translate(-50%, -50%) rotate(-45deg);
    font-family: "Bungee", sans-serif; font-size: 100px; line-height: 1; letter-spacing: 3px;
    color: var(--canvas); -webkit-text-stroke: 8px var(--orange); paint-order: stroke fill;
    white-space: nowrap;
  }

  .divider-rule { position: absolute; left: 228px; right: 38px; top: 903px; height: 6px; background: var(--rule-blue); }

  .claims { position: absolute; left: 440px; top: 0; width: 420px; height: 1139px; font-family: "Oswald", sans-serif; color: var(--ink); }
  .claim { position: absolute; left: 0; font-weight: 500; font-size: 16px; letter-spacing: 0.5px; line-height: 1; white-space: nowrap; }
  .claim--organic { top: 952px; padding-bottom: 6px; border-bottom: 3px solid var(--orange); width: 124px; }
  .claim--sugar { top: 985px; }
  .net-weight { position: absolute; left: 0; top: 1004px; font-weight: 700; font-size: 58px; line-height: 1; white-space: nowrap; }
  .net-weight .unit { font-size: 26px; color: var(--orange); font-weight: 500; }
  .origin { position: absolute; left: 0; top: 1082px; display: flex; align-items: flex-end; gap: 7px; font-weight: 700; font-size: 36px; line-height: 1; white-space: nowrap; }
  .origin .origin-word { font-size: 19px; color: var(--orange); font-weight: 500; padding-bottom: 3px; }
  .origin-flag { width: 28px; height: 28px; margin-bottom: 4px; }
</style>
</head>
<body>
<main class="pouch-front">
  <div class="border-band border-band--top" role="img" aria-label="Yellow border band with African tribal motif pattern"></div>
  <div class="zip-area" role="img" aria-label="Silver foil resealable zip area with fine wavy line texture"></div>

  <svg class="stripe-art" viewBox="0 0 974 1200" aria-hidden="true">
    <g class="stripes-right">
      <line x1="700" y1="700" x2="974" y2="470" stroke="var(--pattern-dark)" stroke-width="88" role="img" aria-label="Geometric tribal pattern panel"/>
      <line x1="791" y1="223" x2="974" y2="395" stroke="var(--orange-soft)" stroke-width="32"/>
      <line x1="796" y1="345" x2="974" y2="505" stroke="var(--maroon)" stroke-width="26"/>
      <line x1="759" y1="782" x2="974" y2="600" stroke="var(--orange-soft)" stroke-width="34"/>
      <line x1="809" y1="699" x2="942" y2="840" stroke="var(--plum)" stroke-width="30"/>
    </g>
    <g class="stripes-left">
      <line x1="0" y1="1085" x2="395" y2="735" stroke="var(--pattern-dark)" stroke-width="88" role="img" aria-label="Geometric tribal pattern panel"/>
      <line x1="0" y1="810" x2="228" y2="930" stroke="var(--maroon)" stroke-width="22"/>
      <line x1="0" y1="610" x2="417" y2="912" stroke="var(--orange-soft)" stroke-width="34"/>
      <line x1="417" y1="912" x2="95" y2="1135" stroke="var(--orange-soft)" stroke-width="30"/>
      <line x1="232" y1="955" x2="345" y2="1040" stroke="var(--maroon)" stroke-width="22"/>
    </g>
  </svg>

  <div class="brand-name">verdyx</div>
  <div class="brand-tagline">Sunshine in Every Bite</div>
  <div class="variant-name">JOLLY PINEAPPLE</div>
  <div class="variant-rule"></div>

  <div class="process-label">DRIED</div>

  <div class="divider-rule"></div>

  <section class="claims">
    <p class="claim claim--organic">100% ORGANIC</p>
    <p class="claim claim--sugar">NO ADDED SUGAR</p>
    <p class="net-weight">100<span class="unit">GM</span></p>
    <p class="origin">
      <svg class="origin-flag" viewBox="0 0 32 32" aria-hidden="true">
        <clipPath id="flag-circle"><circle cx="16" cy="16" r="16"/></clipPath>
        <g clip-path="url(#flag-circle)">
          <rect y="0" width="32" height="6" fill="var(--flag-black)"/>
          <rect y="6" width="32" height="5" fill="var(--flag-yellow)"/>
          <rect y="11" width="32" height="5" fill="var(--flag-red)"/>
          <rect y="16" width="32" height="5" fill="var(--flag-black)"/>
          <rect y="21" width="32" height="5" fill="var(--flag-yellow)"/>
          <rect y="26" width="32" height="6" fill="var(--flag-red)"/>
          <circle cx="16" cy="16" r="6" fill="#ffffff"/>
        </g>
      </svg>
      <span>UGANDAN</span><span class="origin-word">ORIGIN</span>
    </p>
  </section>

  <div class="border-band border-band--bottom" role="img" aria-label="Yellow border band with African tribal motif pattern"></div>
</main>
</body>
</html>
```